KT Prime Motion personal training needs a new Business Card design for 2016

Business Card design:
Our current business card is very plain
We are bringing on our first team member next year and thought its a perfect time to have a new face lift for our company!

We are a Personal Training business "KT Prime Motion" who specializes in strength and conditioning / weightloss training,
We also run a yearly Bootcamp called "Ferocity Drillcamps", this is our Logo Design which we are looking for

The pink and blue in the logo are our business colours, how ever we don't want those colours to heavily dominate the card.

We are looking for a business card which is eye catching, and creative.

I am open to suggestions and any designs :)

Logo Design:

For our Logo Design we are looking for a bright, energetic logo, preferably a word logo which portrays strength and high intensity
If it has icon's etc in it thats fine again im open for suggestions :)
The Logo Design is for our Bootcamp which runs yearly
The bootcamp is called "Ferocity Drillcamp"

Target Market(s)

Age 20-40
Individuals who want to look great and have more energy

Industry/Entity Type

Business

Contact Information for Business Card

On the front
KT Prime Motion Doriel Maxton Personal Training / Bootcamps / Pilates / Nutrition Healthy mind, Healthy body, Ultimate lifestyle < our slogan
Icons for the following
Email:
Mobile:
Facebook:
Instagram:

On the back we would like to include somewhere
"Show this card to receive 50% off your first 30min pt session"
"Valid to one user only"

Logo Text

Ferocity Drillcamp

Font styles to use
Serif

Colors
e34197
0255a3
000000
ffffff

Requirements
Must have
• - Icons for instagram, facebook, email and mobile phone
• - Slogan: Healthy mind, Healthy body, Ultimate lifestyle
• - What we offer: Personal Training , Bootcamps, Pilates, Nutrition
• - Logo
• -
Nice to have
• - Our 50% offer on the back
• - a place for a photo
Should not have
• - Pink and Blue everywhere

```html
<!DOCTYPE html>
<html lang="en">
<head>
<meta charset="utf-8">
<title>KT Prime Motion – Business Card</title>
<link href="https://fonts.googleapis.com/css2?family=Noto+Serif:wght@700&family=Open+Sans:wght@400;600;700&display=swap" rel="stylesheet">
<style>
  :root {
    --page: #ffffff;
    --card-top: #f3f3f4;
    --card-bottom: #c8c8ca;
    --card-back: #f7f8fa;
    --ink: #3a3a3a;
    --ink-soft: #666666;
    --field: #d9dadd;
    --divider: #7a7a7a;
    --photo: #bdbdbd;
    --pink: #e34197;
    --blue: #0255a3;
    --mail: #ea2f6e;
    --phone: #f39325;
    --pin: #222222;
    --insta: #15b2c9;
    --social: #13a89e;
    --white: #ffffff;
  }
  * { box-sizing: border-box; margin: 0; padding: 0; }
  html, body { width: 1200px; height: 417px; overflow: hidden; background: var(--page); }
  .canvas { position: relative; width: 1200px; height: 417px; }

  .card { position: absolute; top: 23px; width: 558px; height: 352px; overflow: hidden; }
  .card--front { left: 25px; background: linear-gradient(to bottom, var(--card-top) 0%, var(--card-top) 45%, var(--card-bottom) 100%); }
  .card--back { left: 616px; width: 559px; background: var(--card-back); }

  .brand { position: absolute; left: 0; width: 282px; top: 122px; text-align: center; font-family: "Open Sans", sans-serif; }
  .brand__mark { display: block; width: 44px; height: 44px; margin: 0 auto 12px; border-radius: 50%; background: var(--pink); }
  .brand__name { font-weight: 700; font-size: 19px; color: var(--ink); letter-spacing: 0.2px; line-height: 1.1; }
  .brand__tagline { font-size: 14px; color: var(--ink); line-height: 1.2; }
  .brand__services { margin-top: 14px; font-size: 9.5px; color: var(--ink-soft); letter-spacing: 0.2px; }

  .slogan { position: absolute; left: 0; width: 282px; top: 304px; text-align: center; font-family: "Noto Serif", serif; font-weight: 700; font-size: 13px; line-height: 17px; color: var(--ink); }

  .divider { position: absolute; left: 268px; top: 53px; width: 2px; height: 245px; background: var(--divider); }

  .photo { position: absolute; left: 306px; top: 28px; width: 64px; height: 64px; border-radius: 50%; background: var(--photo); display: flex; align-items: center; justify-content: center; font-family: "Noto Serif", serif; font-weight: 700; font-size: 9px; color: var(--ink); }

  .person { position: absolute; left: 379px; top: 39px; font-family: "Open Sans", sans-serif; color: var(--ink); white-space: nowrap; }
  .person__name { font-size: 19px; font-weight: 400; line-height: 1; letter-spacing: 0.2px; }
  .person__name strong { font-weight: 700; }
  .person__role { font-size: 12px; color: var(--ink-soft); margin-top: 3px; }

  .contacts { position: absolute; left: 307px; top: 110px; list-style: none; }
  .contact { display: flex; height: 36px; margin-bottom: 8.6px; }
  .contact__icon { width: 36px; height: 36px; display: flex; align-items: center; justify-content: center; }
  .contact__icon--mail { background: var(--mail); }
  .contact__icon--phone { background: var(--phone); }
  .contact__icon--pin { background: var(--pin); }
  .contact__icon--insta { background: var(--insta); }
  .contact__icon--social { background: var(--social); }
  .contact__dot { width: 14px; height: 14px; background: var(--white); border-radius: 50%; }
  .contact__block { width: 14px; height: 14px; background: var(--white); }
  .contact__text { width: 137px; margin-left: 4px; background: var(--field); font-family: "Open Sans", sans-serif; font-size: 9.5px; line-height: 11px; color: var(--ink-soft); display: flex; flex-direction: column; justify-content: center; padding-left: 11px; white-space: nowrap; }

  .offer { position: absolute; left: 0; width: 100%; top: 20px; text-align: center; font-family: "Noto Serif", serif; font-weight: 700; font-size: 12.5px; line-height: 16px; color: var(--ink); }
  .offer__highlight { font-size: 16.5px; }
</style>
</head>
<body>
<div class="canvas">
  <section class="card card--front">
    <div class="brand">
      <span class="brand__mark"></span>
      <div class="brand__name">KT PRIME MOTION</div>
      <div class="brand__tagline">Power Your Body</div>
      <div class="brand__services">Personal Training · Bootcamps · Pilates · Nutrition</div>
    </div>
    <p class="slogan">Healthy Mind, Healthy Body<br>Ultimate Lifestyle</p>
    <div class="divider"></div>

    <div class="photo" role="img" aria-label="Portrait photo of the trainer">PHOTO</div>
    <div class="person">
      <div class="person__name">DORIEL <strong>MAXTON</strong></div>
      <div class="person__role">Personal Trainer</div>
    </div>

    <ul class="contacts">
      <li class="contact">
        <span class="contact__icon contact__icon--mail">
          <svg width="22" height="16" viewBox="0 0 22 16"><rect x="0.5" y="0.5" width="21" height="15" rx="1.5" fill="#fff"/><path d="M1 1.5 L11 9 L21 1.5" fill="none" stroke="#ea2f6e" stroke-width="1.6"/></svg>
        </span>
        <span class="contact__text"><span>Your address here</span><span>Lorem Ipsum</span></span>
      </li>
      <li class="contact">
        <span class="contact__icon contact__icon--phone">
          <svg width="20" height="20" viewBox="0 0 24 24"><path d="M6.6 10.8a15.1 15.1 0 0 0 6.6 6.6l2.2-2.2c.3-.3.7-.4 1-.2 1.1.4 2.3.6 3.6.6.6 0 1 .4 1 1V20c0 .6-.4 1-1 1C10.6 21 3 13.4 3 4c0-.6.4-1 1-1h3.5c.6 0 1 .4 1 1 0 1.3.2 2.5.6 3.6.1.3 0 .7-.2 1z" fill="#fff"/></svg>
        </span>
        <span class="contact__text"><span>T. 123 456 789</span><span>M. 123 456 789</span></span>
      </li>
      <li class="contact">
        <span class="contact__icon contact__icon--pin">
          <svg width="16" height="24" viewBox="0 0 16 24"><path d="M8 0.5A7.5 7.5 0 0 0 .5 8c0 5.6 7.5 15.5 7.5 15.5S15.5 13.6 15.5 8A7.5 7.5 0 0 0 8 .5z" fill="#fff"/><circle cx="8" cy="8" r="3" fill="#222"/></svg>
        </span>
        <span class="contact__text"><span>www.primemotionfit.com</span></span>
      </li>
      <li class="contact">
        <span class="contact__icon contact__icon--insta" role="img" aria-label="Photo sharing profile"><span class="contact__dot"></span></span>
        <span class="contact__text"><span>hello@primemotionfit.com</span></span>
      </li>
      <li class="contact">
        <span class="contact__icon contact__icon--social" role="img" aria-label="Social network profile"><span class="contact__block"></span></span>
        <span class="contact__text"><span>hello@primemotionfit.com</span></span>
      </li>
    </ul>
  </section>

  <section class="card card--back">
    <p class="offer">Show this card to receive <span class="offer__highlight">50% OFF</span>&nbsp; your first 30 min point session<br>Valid to one user only</p>
  </section>
</div>
</body>
</html>
```